Brinevale Yacht Management Full Page Ad Flyer

Yacht Management Package also includes the following periodic Monthly services:

Monthly full vessel systems checklist inspections
Diver For Hull Cleaning And Inspection Of Props, Shafts, and Zincs
Interior/Exterior Detailing and scheduled washdowns
Manage Haulout
Pump-out Services
On-call Captain and Crew Services
Updates

Need more time to provide more content to designers and the printing press template file.

Target Market(s)

Vessel owners, motor yachts, sailboats from 25 feet in length up to 125 feet in length. We do not do cruise ships or yachts larger than 125 feet. Someone who has their boat docked at their house or a local marina. We also offer mobile on-site services.

```html
<!DOCTYPE html>
<html lang="en">
<head>
<meta charset="utf-8">
<title>Brinevale Yacht Management – Full Page Ad</title>
<link href="https://fonts.googleapis.com/css2?family=Bebas+Neue&family=Itim&display=swap" rel="stylesheet">
<style>
  :root {
    --navy: #2c3c68;
    --navy-deep: #27365f;
    --cyan: #1fa7d4;
    --white: #ffffff;
    --ink: #2b3a66;
    --body-ink: #5c6470;
    --page-bg: #dfe9f1;
    --sky: #e8f2f9;
    --sea: #2e7fae;
  }
  * { margin: 0; padding: 0; box-sizing: border-box; }
  html, body { width: 1200px; height: 1200px; overflow: hidden; background: var(--page-bg); }
  .flyer {
    position: absolute; left: 190px; top: 20px;
    width: 820px; height: 1160px;
    background: var(--white);
    box-shadow: 0 12px 30px rgba(40, 60, 90, 0.18);
    overflow: hidden;
  }
  .flyer-shapes { position: absolute; inset: 0; width: 100%; height: 100%; }
  .inner-frame {
    position: absolute; inset: 6px;
    border: 1px solid #555b66; pointer-events: none;
  }
  .headline {
    position: absolute; left: 27px;
    font-family: "Bebas Neue", "Oswald", sans-serif;
    color: var(--ink); line-height: 1; white-space: nowrap;
  }
  .headline--main { top: 61px; font-size: 42px; }
  .headline--sub { top: 120px; font-size: 30px; }
  .rule { position: absolute; left: 0; height: 3px; background: var(--cyan); }
  .rule--main { top: 107px; width: 420px; }
  .rule--sub { top: 151px; width: 331px; }
  .intro {
    position: absolute; left: 27px; top: 162px; width: 304px;
    font-family: "Itim", sans-serif; font-size: 9.3px; line-height: 12.3px;
    color: var(--body-ink); text-align: justify;
  }
  .brand {
    position: absolute; left: 411px; top: 625px; transform: translateX(-50%);
    text-align: center; color: var(--white);
    font-family: "Bebas Neue", "Oswald", sans-serif; font-weight: 400;
    line-height: 1; white-space: nowrap;
  }
  .brand-name { display: block; font-size: 88px; letter-spacing: 6px; }
  .brand-sub { display: block; font-size: 30px; letter-spacing: 9px; margin-top: 4px; }
  .services-tab {
    position: absolute; left: 591px; top: 891px; width: 229px; height: 41px;
    background: linear-gradient(90deg, rgba(39,54,95,0) 0%, var(--navy-deep) 18%, #33467a 100%);
    display: flex; align-items: center; justify-content: flex-end; padding-right: 20px;
    font-family: "Bebas Neue", "Oswald", sans-serif; font-size: 27px; color: var(--white);
  }
  .services-list {
    position: absolute; left: 45px; top: 958px; list-style: none;
    font-family: "Bebas Neue", "Oswald", sans-serif; font-size: 27px;
    line-height: 32px; color: var(--cyan); white-space: nowrap;
  }
  .services-list li::before { content: "• "; }
</style>
</head>
<body>
  <main class="flyer">
    <svg class="flyer-shapes" viewBox="0 0 1215 1712" preserveAspectRatio="none" aria-hidden="false">
      <defs>
        <linearGradient id="photoTone" x1="0" y1="0" x2="0" y2="1">
          <stop offset="0" stop-color="#eef6fb"/>
          <stop offset="0.55" stop-color="#d6e8f3"/>
          <stop offset="1" stop-color="#2e7fae"/>
        </linearGradient>
      </defs>
      <polygon class="hero-photo" role="img" aria-label="Photo of a white motor yacht cutting through blue water, with palm fronds in the top right corner" points="0,0 1215,0 1215,720 0,905" fill="url(#photoTone)"/>
      <polygon class="brand-band" points="0,935 1215,730 1215,1390 0,1390" fill="#2c3c68"/>
      <polygon class="accent-stripe" points="0,1225 1215,1103 1215,1152 0,1365" fill="#1fa7d4"/>
      <polygon class="accent-line" points="0,1378 1215,1163 1215,1173 0,1388" fill="#ffffff"/>
    </svg>
    <div class="inner-frame"></div>

    <h1 class="headline headline--main">Keep your yacht pristine,</h1>
    <div class="rule rule--main"></div>
    <h2 class="headline headline--sub">Let us handle the details.</h2>
    <div class="rule rule--sub"></div>
    <p class="intro">Hiring a professional yacht management service ensures your vessel stays in peak condition with expert maintenance, regular inspections, and thorough cleaning. You save time by leaving detailing, haulout coordination, and pump-out services to professionals, allowing you to focus on enjoying your yacht. With on-call crew services and timely care, you gain peace of mind while protecting your yacht’s longevity and value.</p>

    <div class="brand">
      <span class="brand-name">Brinevale</span>
      <span class="brand-sub">Yacht Management</span>
    </div>

    <div class="services-tab">Services we offer :</div>
    <ul class="services-list">
      <li>Monthly full vessel systems checklist inspections</li>
      <li>Diver for hull cleaning and inspection of props, shafts, and zincs</li>
      <li>Interior/exterior detailing and scheduled washdowns</li>
      <li>Manage haulout</li>
      <li>Pump-out services</li>
      <li>On-call captain and crew services</li>
    </ul>
  </main>
</body>
</html>
```